Niche Fitness Rebrand : Q7 Peak Conditioning

We're re-branding our fitness business and need to develop a cleaner, more sophisticated, and sleek website for our clients and potential clients to reference. We're looking to have some photo presence on all pages, with clean, crisp sections for easy reading on the web, and on mobile. We love the BRXpdx(.com) website, which represents a very similar target market, and one of the same methods that our business represents. We're looking to take this local studio to a more professional level for future expansion, and need it to be sleek and in line with the growing and competitive marketplace for fitness.
Target Market(s)
70/30 women to men, physically active, upper middle class / professional between the ages of 28-42.
Industry/Entity Type
Fitness
Coding
Coded - Design and coding required
Number of Pages Required
5+ page
Requirements
Must have
- sleek, professional, high-end design, with easy user navigation.
- About Page - with drop down child pages for management and coaches bios
- Classes Page 'The Methods' - with drop down child pages for different class types
- Location / Schedule Page
- Pricing
- Blog
- Private staff only programming login page
Nice to have
- potential to add an online retail shop -- but not currently necessary.
- Industry websites we like:
- www.brxpdx.com
- www.torvanaclub.com

```html
<!DOCTYPE html>
<html lang="en">
<head>
<meta charset="utf-8">
<title>Q7 Peak Conditioning</title>
<link href="https://fonts.googleapis.com/css2?family=Lato:wght@300;400;700;900&family=Oswald:wght@500;600&display=swap" rel="stylesheet">
<style>
:root{
  --ink:#1b1b1b;
  --muted:#6a6a6a;
  --tan:#b8976a;
  --tan-line:#d6bf99;
  --light:#ececec;
  --white:#ffffff;
  --black:#0d0d0d;
  --dark-tab:#2a2a2a;
}
*{box-sizing:border-box;margin:0;padding:0}
html,body{width:1200px;height:3622px;overflow:hidden}
body{font-family:'Lato',sans-serif;color:var(--ink);background:var(--white);position:relative}
section,header,footer{position:absolute;left:0;width:1200px}
.frame-btn{position:absolute;display:flex;align-items:center;justify-content:center;font-weight:700;text-transform:uppercase;letter-spacing:.5px}
/* header */
.site-header{top:0;height:101px;background:var(--white);display:flex;align-items:center;padding:0 77px}
.brand{display:flex;align-items:center;gap:14px}
.brand-mark{width:42px;height:42px;border:0;background:var(--ink)}
.brand-name{font-weight:700;font-size:28px;line-height:30px;color:var(--ink);text-transform:uppercase}
.main-nav{margin-left:auto;display:flex;gap:38px;font-size:14px;text-transform:uppercase;color:var(--ink)}
.nav-tools{display:flex;align-items:center;gap:14px;margin-left:38px}
/* hero */
.hero{top:101px;height:578px;background:linear-gradient(100deg,#4a4a4a 0%,#6a6a6a 45%,#5c5c5c 75%,#3e3e3e 100%)}
.hero-title{position:absolute;left:80px;top:186px;font-family:'Oswald',sans-serif;font-weight:600;font-size:37px;color:var(--white);letter-spacing:.5px}
.hero-sub{position:absolute;left:80px;top:236px;font-size:22px;color:#f1f1f1}
.hero .frame-btn{left:80px;top:297px;width:258px;height:104px;border:14px solid var(--white);color:var(--white);font-size:22px;background:rgba(40,40,40,.4)}
.polaroid{position:absolute;background:var(--white);padding:10px 10px 26px;box-shadow:0 4px 12px rgba(0,0,0,.35)}
.polaroid .ph{width:100%;height:100%}
.hero-dots{position:absolute;left:560px;top:534px;display:flex;gap:6px}
.hero-dots i{width:11px;height:11px;border:2px solid var(--white);display:block}
.hero-dots i.on{background:var(--white)}
/* about */
.about{top:679px;height:364px;background:var(--light);text-align:center}
.about h2{position:absolute;left:0;right:0;top:62px;font-size:42px;font-weight:400}
.about p{position:absolute;left:230px;right:230px;top:126px;font-size:13px;line-height:22px;color:var(--muted)}
.about .frame-btn{left:500px;top:224px;width:200px;height:58px;border:7px solid var(--ink);border-left-width:12px;font-size:18px;font-weight:400}
.about-photo{position:absolute;top:0;height:364px}
/* classes */
.classes{top:1043px;height:659px;background:var(--white)}
.section-title{position:absolute;left:0;right:0;text-align:center;font-size:38px;font-weight:700}
.class-grid{position:absolute;left:77px;top:119px;width:1046px;display:grid;grid-template-columns:repeat(3,344px);grid-template-rows:222px 222px;gap:7px 7px}
.class-photo{position:relative}
.class-photo span{position:absolute;left:0;right:0;top:96px;text-align:center;color:var(--white);font-size:28px}
.class-card{background:var(--tan);padding:18px;position:relative}
.class-card .inner{border:8px solid var(--tan-line);height:100%;text-align:center;padding:24px 26px 0;color:var(--white)}
.class-card h3{font-size:24px;font-weight:400;color:var(--ink);margin-bottom:8px}
.class-card p{font-size:13px;line-height:18px}
.class-card a{display:inline-block;margin-top:8px;font-size:15px;font-weight:700;color:var(--ink);text-decoration:underline}
.class-dots{position:absolute;left:573px;top:596px;display:flex;gap:8px}
.class-dots i{width:11px;height:11px;border:2px solid var(--ink);display:block}
/* trainers */
.trainers{top:1702px;height:604px;background:var(--light)}
.trainers .lead{position:absolute;left:175px;right:175px;top:118px;text-align:center;font-size:13px;line-height:20px;color:var(--muted)}
.trainer-tabs{position:absolute;left:220px;width:760px;top:175px;display:flex;justify-content:space-around;font-size:17px;color:var(--muted);border-bottom:2px solid #7a7a7a;padding-bottom:10px}
.trainer-tabs .on{color:var(--tan)}
.trainer-photo{position:absolute;left:152px;top:305px;width:295px;height:246px}
.trainer-about h3{position:absolute;left:478px;top:325px;font-size:30px;font-weight:400;letter-spacing:.5px}
.trainer-about p{position:absolute;left:478px;top:374px;width:570px;font-size:13px;line-height:23px;color:var(--muted)}
.trainers .frame-btn{left:478px;top:471px;width:220px;height:61px;border:7px solid var(--ink);border-left-width:12px;font-size:17px;font-weight:400}
/* pricing */
.pricing{top:2306px;height:380px;background:var(--white)}
.price-table{position:absolute;left:157px;top:119px;width:886px;height:207px;display:flex}
.price-special{width:174px;background:var(--black);position:relative}
.price-special .box{position:absolute;left:48px;top:38px;width:90px;height:132px;border:8px solid var(--white);display:flex;align-items:center;justify-content:center}
.price-special .box span{transform:rotate(-90deg);white-space:nowrap;color:var(--white);font-size:24px;font-weight:700;line-height:24px;text-align:center}
.price-cell{width:197px;background:var(--tan);text-align:center;padding-top:38px;color:var(--ink);border-left:2px solid #d9c6a4}
.price-cell .label{font-size:20px;line-height:22px}
.price-cell .amount{font-size:42px;font-weight:700;color:var(--white);margin-top:18px}
.price-tab{width:79.5px;background:var(--dark-tab);border-left:3px solid #555;display:flex;align-items:center;justify-content:center}
.price-tab span{transform:rotate(-90deg);white-space:nowrap;color:var(--white);font-size:22px}
/* shop */
.shop{top:2686px;height:471px;background:linear-gradient(90deg,#2c3035 0%,#3d4c52 40%,#557a82 70%,#2c3a3d 100%)}
.shop h2{position:absolute;left:80px;top:106px;font-size:50px;font-weight:700;color:var(--white);letter-spacing:1px}
.shop p{position:absolute;left:80px;top:180px;width:680px;font-size:15px;line-height:22px;color:#eaeaea}
.shop a{position:absolute;left:80px;top:263px;font-size:29px;font-weight:700;color:var(--white);text-decoration:underline}
/* footer */
.site-footer{top:3157px;height:383px;background:var(--light)}
.footer-col{position:absolute;top:62px}
.footer-col h4{font-size:22px;font-weight:400;margin-bottom:30px}
.post{display:flex;gap:20px;margin-bottom:28px}
.post-date{text-align:center;width:40px}
.post-date b{display:block;font-size:30px;font-weight:400;line-height:30px}
.post-date small{font-size:14px}
.post h5{font-size:17px;font-weight:400;margin-bottom:6px}
.post p{font-size:13px;line-height:18px;color:var(--muted);width:230px}
.post em{font-style:normal;font-size:11px;color:#9a9a9a}
.newsletter p{font-size:13px;line-height:19px;color:var(--muted);width:330px}
.newsletter .field{margin-top:44px;width:312px;height:46px;border:1px solid #555;background:var(--white);font-size:13px;padding:15px 14px;color:var(--ink)}
.newsletter .frame-btn{position:relative;margin-top:16px;width:222px;height:62px;border:7px solid var(--ink);border-left-width:12px;font-size:19px;font-weight:400}
.contact-row{display:flex;gap:14px;font-size:13px;line-height:18px;color:var(--muted);margin-bottom:24px}
.socials{display:flex;gap:6px;margin-left:16px}
.socials i{width:24px;height:24px;border-radius:50%;border:2px solid var(--ink);display:block}
.socials i:first-child{background:var(--tan);border-color:var(--tan)}
.copyright{position:absolute;top:3540px;left:0;width:1200px;height:82px;background:var(--black);color:var(--white);font-size:15px;display:flex;align-items:center;justify-content:center;gap:6px}
.copyright b{color:var(--tan)}
</style>
</head>
<body>

<header class="site-header">
  <div class="brand"><div class="brand-mark"></div><div class="brand-name">Q7 Peak<br>Conditioning</div></div>
  <nav class="main-nav"><span>Home</span><span>About Us</span><span>Classes</span><span>Pricing</span><span>Blogs</span><span>Contact Us</span></nav>
  <div class="nav-tools">
    <svg width="24" height="24" viewBox="0 0 24 24"><circle cx="12" cy="12" r="10" fill="none" stroke="#1b1b1b" stroke-width="3"/><path d="M12 6v6l4 2" stroke="#1b1b1b" stroke-width="2" fill="none"/></svg>
    <svg width="2" height="28"><rect width="2" height="28" fill="#999"/></svg>
    <svg width="30" height="26" viewBox="0 0 30 26"><path d="M1 3h5l4 14h14l4-10H8" fill="none" stroke="#1b1b1b" stroke-width="2.4"/><circle cx="12" cy="22" r="2.2" fill="#1b1b1b"/><circle cx="22" cy="22" r="2.2" fill="#1b1b1b"/></svg>
  </div>
</header>

<section class="hero">
  <h1 class="hero-title">OUR FUN-FILLED GROUP CLASSES</h1>
  <div class="hero-sub">Pilates, Yoga, Rhythmix, Meditation...</div>
  <div class="frame-btn">See All Classes</div>
  <div class="polaroid" style="left:660px;top:118px;width:222px;height:246px;transform:rotate(-4deg)"><div class="ph" role="img" aria-label="Photo of a group fitness class" style="background:linear-gradient(#c9b49c,#8f7a66)"></div></div>
  <div class="polaroid" style="left:860px;top:92px;width:196px;height:214px;transform:rotate(4deg)"><div class="ph" role="img" aria-label="Photo of gym equipment" style="background:linear-gradient(#9aa0a6,#5a5f66)"></div></div>
  <div class="polaroid" style="left:776px;top:254px;width:232px;height:248px;transform:rotate(-2deg)"><div class="ph" role="img" aria-label="Photo of a class doing leg lifts" style="background:linear-gradient(#b9ac9c,#7d6e5f)"></div></div>
  <div class="hero-dots"><i></i><i></i><i class="on"></i><i></i></div>
</section>

<section class="about">
  <div class="about-photo" role="img" aria-label="Photo of a woman training on a cable machine" style="left:0;width:250px;background:linear-gradient(90deg,#d7d7d7,#b4aaa0 55%,#e8e8e8)"></div>
  <div class="about-photo" role="img" aria-label="Photo of a woman swinging a kettlebell" style="right:0;width:250px;background:linear-gradient(90deg,#e8e8e8,#7c7a74 50%,#2f3a2c)"></div>
  <h2>About Us</h2>
  <p>Lorem ipsum dolor sit amet, consectetur adipiscing elit, sed do eiusmod tempor incididunt ut labore et dolore magna aliqua. Ut enim ad minim veniam, quis nostrud exercitation ullamco laboris nisi ut aliquip ex ea commodo consequat. Duis aute irure dolor in reprehenderit in voluptate</p>
  <div class="frame-btn">Read More</div>
</section>

<section class="classes">
  <h2 class="section-title" style="top:48px">Fun Filled Classes</h2>
  <div class="class-grid">
    <div class="class-photo" role="img" aria-label="Photo of a reformer pilates class" style="background:linear-gradient(#8fb6c4,#5d6d74)"></div>
    <div class="class-card"><div class="inner"><h3>Rowing</h3><p>Our signature core training method using slow and controlled movements under a spring loaded system...</p><a>Read More</a></div></div>
    <div class="class-photo" role="img" aria-label="Photo of a man on a rowing machine" style="background:linear-gradient(#3d3f42,#151618)"></div>
    <div class="class-card"><div class="inner"><h3>Spanformer</h3><p>Our signature core training method using slow and controlled movements under a spring loaded system...</p><a>Read More</a></div></div>
    <div class="class-photo" role="img" aria-label="Photo of a woman balancing on a stability ball" style="background:linear-gradient(#5c5c5c,#2b2b2b)"><span>Core</span></div>
    <div class="class-card"><div class="inner"><h3>Core</h3><p>Our signature core training method using slow and controlled movements under a spring loaded system...</p><a>Read More</a></div></div>
  </div>
  <div class="class-dots"><i></i><i></i><i></i></div>
</section>

<section class="trainers">
  <h2 class="section-title" style="top:50px">Certified Trainers</h2>
  <p class="lead">Our personal trainers are certified professionals who will educate, motivate and keep you accountable. If you are new to exercise or having trouble staying fit, you need a personal trainer. Our goal is to get you exercising regularly and obtain results you want.</p>
  <div class="trainer-tabs"><span>Dorian Pell</span><span>Marta Quill</span><span class="on">Lena Varsh</span><span>Owen Castry</span></div>
  <div class="trainer-photo" role="img" aria-label="Portrait photo of trainer Lena Varsh" style="background:linear-gradient(#c7b8a6,#7b6b5b);border:6px solid #fff"></div>
  <div class="trainer-about">
    <h3>About Lena Varsh</h3>
    <p>Lundium porta turpis est facilisis velit, ut pellentesque, est et hac, sit. Ridiculus quis, in, magnis! Aenean nec cum tincidunt, velit est, nisi rhoncus. Aliquet odio pellentesque! Sociis nunc pid in quis mauris auctor tristique ridiculus augue cras rhoncus, adipiscing dolor pellentesque. Dictumst nisi est phasellus placerat, dictumst ac.</p>
  </div>
  <div class="frame-btn">See Trainer Bio</div>
</section>

<section class="pricing">
  <h2 class="section-title" style="top:48px">Pricing</h2>
  <div class="price-table">
    <div class="price-special"><div class="box"><span>New Client<br>Special</span></div></div>
    <div class="price-cell"><div class="label">New Client<br>1 Class</div><div class="amount">$15</div></div>
    <div class="price-cell"><div class="label">New Client<br>15 Days Unlimited</div><div class="amount">$55</div></div>
    <div class="price-tab"><span>Class Packages</span></div>
    <div class="price-tab"><span>Contract Pricing</span></div>
    <div class="price-tab"><span>1 Month Pricing</span></div>
    <div class="price-tab"><span>Student Pricing</span></div>
  </div>
</section>

<section class="shop" role="img" aria-label="Photo of the studio shop with apparel racks">
  <h2>OUR SHOP</h2>
  <p>Lorem ipsum dolor sit amet, consectetur adipiscing elit, sed do eiusmod tempor Lorem ipsum dolor sit amet, consectetur adipiscing elit, sed do eiusmod tempor.Lorem ipsum dolor sit amet, consectetur adipiscing elit, sed do eiusmod tempor.</p>
  <a>SHOP NOW »</a>
</section>

<footer class="site-footer">
  <div class="footer-col" style="left:80px">
    <h4>Latest From Blog</h4>
    <div class="post"><div class="post-date"><b>30</b><small>May</small></div><div><h5>Lorem ipsum dolor</h5><p>Lorem ipsum dolor sit, consectetur adipiscing elit amet.</p><em>Post On 30th May, 2017</em></div></div>
    <div class="post"><div class="post-date"><b>25</b><small>May</small></div><div><h5>Lorem ipsum dolor</h5><p>Lorem ipsum dolor sit, consectetur adipiscing elit amet.</p><em>Post On 25th May, 2017</em></div></div>
  </div>
  <div class="footer-col newsletter" style="left:442px">
    <h4>Newsletter</h4>
    <p>Lorem ipsum dolor sit amet, consectetur adipiscing elit, sed do eiusmod tempor</p>
    <div class="field">Email</div>
    <div class="frame-btn">Submit</div>
  </div>
  <div class="footer-col" style="left:812px">
    <h4>Keep in Touch</h4>
    <div class="contact-row"><svg width="14" height="18" viewBox="0 0 14 18"><path d="M7 1a6 6 0 0 1 6 6c0 4-6 10-6 10S1 11 1 7a6 6 0 0 1 6-6z" fill="none" stroke="#b8976a" stroke-width="1.6"/><circle cx="7" cy="7" r="2" fill="#b8976a"/></svg><span>Q7 PEAK CONDITIONING<br>418 Alder Row NE<br>Millbrook, OR 97410</span></div>
    <div class="contact-row"><svg width="14" height="16" viewBox="0 0 14 16"><path d="M3 1l3 3-2 2c1 2 3 4 5 5l2-2 3 3-2 3C6 14 1 8 0 3z" fill="none" stroke="#b8976a" stroke-width="1.4"/></svg><span>+1 555 014 2290</span></div>
    <div class="contact-row"><svg width="16" height="14" viewBox="0 0 16 14"><path d="M1 6l14-5-4 12-3-5z" fill="none" stroke="#b8976a" stroke-width="1.4"/></svg><span>millbrook@q7peak.example</span></div>
    <div class="socials"><i></i><i></i><i></i></div>
  </div>
</footer>

<div class="copyright">© <b>Q7 PEAK CONDITIONING</b> - 2017. All Rights reserved.</div>

</body>
</html>
```